New modern website for Kerbline Groundworks

Hi we are an existing company that has a current website http://www.kerblinegroundworks.co.nz/ we are looking to get a new vibrant looking website designed to take us further and gain more customers. We are after a simple easy to use website that does not confuse but we want to make an impact and stand out from the rest

Target Market(s)

Homeowners And Commercial Businesses

Industry/Entity Type

It Company

Coding

Coded - Design and coding required

Number of Pages Required

2 page

```html
<!DOCTYPE html>
<html lang="en">
<head>
<meta charset="utf-8">
<title>Kerbline Groundworks</title>
<link rel="stylesheet" href="https://fonts.googleapis.com/css2?family=Jost:wght@600&family=Open+Sans:wght@400;600&family=Raleway:wght@400;500;700&display=swap">
<style>
:root{
  --yellow:#fcd200;
  --yellow-deep:#f2b705;
  --ink:#2b2b2b;
  --charcoal:#2e2e2e;
  --grey-text:#8a8a8a;
  --nav:#555;
  --white:#fff;
}
*{box-sizing:border-box;margin:0;padding:0}
html,body{width:678px;height:1200px;overflow:hidden;background:var(--white)}
body{position:relative;font-family:"Open Sans",sans-serif;color:var(--ink)}
h1,h2,h3{font-weight:400}
.abs{position:absolute}

/* header */
.site-header{left:0;top:0;width:678px;height:58px;background:var(--white)}
.brand{left:76px;top:22px;display:flex;align-items:center;gap:6px;font-family:"Raleway",sans-serif;font-weight:700;font-size:13px;color:var(--ink);letter-spacing:.3px}
.brand-mark{width:10px;height:10px;background:var(--ink)}
.main-nav{left:252px;top:27px;font-family:"Raleway",sans-serif;font-size:8.5px;color:var(--nav)}
.main-nav a{color:inherit;text-decoration:none;position:absolute;white-space:nowrap}
.main-nav a.active{color:var(--yellow-deep)}
.header-phone{left:524px;top:22px;display:flex;align-items:center;gap:5px;font-family:"Raleway",sans-serif;font-size:10.5px;font-weight:500}
.phone-dot{width:15px;height:15px;border-radius:50%;background:var(--yellow);display:flex;align-items:center;justify-content:center}

/* hero */
.hero{left:0;top:58px;width:678px;height:294px;background:linear-gradient(180deg,#7a7f6a 0%,#4d4a44 35%,#2a2826 70%,#1e1d1c 100%)}
.hero-title{left:0;top:100px;width:678px;text-align:center;font-family:"Jost",sans-serif;font-weight:600;font-size:22px;line-height:27px;color:var(--white);letter-spacing:.3px}
.hero-title .accent{color:var(--yellow)}
.hero-arrow{top:124px}

/* intro */
.intro-divider{left:262px;top:378px;width:144px;height:2px;background:#333}
.intro-heading{left:0;top:387px;width:678px;text-align:center;font-family:"Raleway",sans-serif;font-weight:400;color:#4a4a4a}
.intro-heading .line1{font-size:16px;display:block;line-height:20px}
.intro-heading .line2{font-size:13px;display:block;line-height:19px}
.intro-copy{left:104px;top:434px;width:470px;text-align:center;font-size:7.5px;line-height:13.3px;color:var(--grey-text)}
.btn-dark{left:305px;top:484px;width:67px;height:23px;background:var(--charcoal);color:var(--white);font-size:8px;display:flex;align-items:center;justify-content:center}

/* services band */
.services-band{left:0;top:538px;width:678px;height:201px;background:radial-gradient(circle at 50% 40%,#dcdcdc,#bdbdbd)}
.service-card{top:560px;width:168px;height:163px}
.service-card svg.card-shape{position:absolute;left:0;top:0}
.service-icon{position:absolute;left:50px;top:2px;width:68px;height:68px;border-radius:50%;background:var(--yellow);border:2px solid var(--white);display:flex;align-items:center;justify-content:center}
.service-title{position:absolute;left:0;top:79px;width:168px;text-align:center;font-family:"Raleway",sans-serif;font-size:12.5px;color:var(--white)}
.service-copy{position:absolute;left:0;top:98px;width:168px;text-align:center;font-size:6.5px;line-height:11px;color:#bbb}
.btn-outline{position:absolute;left:53px;top:129px;width:63px;height:20px;border:1px solid var(--white);color:var(--white);font-size:7.5px;display:flex;align-items:center;justify-content:center}

/* projects */
.projects-band{left:0;top:739px}
.projects-heading{left:0;top:764px;width:678px;text-align:center;font-family:"Raleway",sans-serif;font-weight:400;font-size:15px;color:var(--ink)}
.project-thumb{top:794px;width:126px;height:92px;border:3px solid var(--white)}
.slider-dots{left:324px;top:905px;display:flex;gap:2px}
.slider-dots span{width:6px;height:6px;border-radius:50%;background:var(--ink)}
.slider-dots span.off{background:transparent;border:1px solid var(--white)}

/* lower */
.feature-image{top:994px;width:120px;height:80px}
.feature-title{top:990px;font-family:"Raleway",sans-serif;font-weight:400;font-size:12.5px;color:var(--ink)}
.feature-copy{top:1009px;font-size:6.7px;line-height:13px;color:var(--grey-text)}
.read-more{left:212px;top:1063px;font-size:6.7px;font-weight:600;color:#666;letter-spacing:.3px}
.contact-line{display:flex;align-items:center;gap:5px;color:#555}

/* footer */
.site-footer{left:0;top:1132px;width:678px;height:68px;background:var(--charcoal)}
.footer-nav{top:1152px;font-family:"Raleway",sans-serif;font-size:8.5px;color:#ddd}
.copyright{left:91px;top:1170px;font-size:6.5px;color:#ccc}
.social{top:1151px;width:18px;height:18px;border-radius:50%;background:var(--yellow-deep);border:1.5px solid var(--white)}
</style>
</head>
<body>

<header class="site-header abs">
  <div class="brand abs"><span class="brand-mark"></span>Kerbline Groundworks</div>
  <nav class="main-nav abs">
    <a class="active" style="left:0">HOME</a>
    <a style="left:44px">ABOUT</a>
    <a style="left:93px">SERVICES</a>
    <a style="left:152px">PROJECTS</a>
    <a style="left:213px">CONTACT</a>
  </nav>
  <div class="header-phone abs">
    <span class="phone-dot"><svg width="8" height="8" viewBox="0 0 24 24"><path fill="#fff" d="M6.6 10.8a15 15 0 006.6 6.6l2.2-2.2a1 1 0 011-.25 11.4 11.4 0 003.6.6 1 1 0 011 1V20a1 1 0 01-1 1A17 17 0 013 4a1 1 0 011-1h3.5a1 1 0 011 1c0 1.25.2 2.45.6 3.6a1 1 0 01-.25 1z"/></svg></span>
    09 418 2260
  </div>
</header>

<section class="hero abs" role="img" aria-label="Road worker spreading fresh asphalt with rollers in the background"></section>
<h1 class="hero-title abs">SETTING THE STARNDARD FOR QUALITY<br><span class="accent">CONCRETE &amp; ASPHALTERS</span></h1>
<svg class="hero-arrow abs" style="left:60px" width="12" height="22" viewBox="0 0 12 22"><path d="M10 2 2 11l8 9" stroke="#fff" stroke-width="2.2" fill="none"/></svg>
<svg class="hero-arrow abs" style="left:606px" width="12" height="22" viewBox="0 0 12 22"><path d="M2 2l8 9-8 9" stroke="#fff" stroke-width="2.2" fill="none"/></svg>

<div class="intro-divider abs"></div>
<h2 class="intro-heading abs"><span class="line1">HE TRUSTED NAME FOR ALL CONCRETE &amp;</span><span class="line2">ASPHALT PAVING IN AUCKLAND</span></h2>
<p class="intro-copy abs">Cras a ante vitae enim iaculis aliquam Mauris nunc quam venenatis nec euismod sit amet egestas placerat est Pellentesque habitant morbi tristique senectus et netus et malesuada fames ac turpis egestas Cras id elit Integer quis urna Ut ante enim dapibus malesuada fringilla eu condimentum</p>
<div class="btn-dark abs">Read More</div>

<section class="services-band abs" role="img" aria-label="Concrete surface texture"></section>

<div class="service-card abs" style="left:84px">
  <svg class="card-shape" width="168" height="163" viewBox="0 0 168 163"><path d="M0 20Q84 -10 168 20V163H0z" fill="var(--charcoal)"/></svg>
  <div class="service-icon"><svg width="32" height="36" viewBox="0 0 32 36"><path d="M9 20l-4 14 5-3 3 4 3-13zM23 20l4 14-5-3-3 4-3-13z" fill="#222"/><circle cx="16" cy="13" r="11" fill="#222"/><circle cx="16" cy="13" r="7" fill="none" stroke="var(--yellow)" stroke-width="1.5"/><path d="M16 8l1.5 3.3 3.5.4-2.6 2.4.7 3.5-3.1-1.8-3.1 1.8.7-3.5-2.6-2.4 3.5-.4z" fill="var(--yellow)"/></svg></div>
  <div class="service-title">Our Expertise</div>
  <div class="service-copy">Cras a ante vitae enim iaculis aliquam<br>Mauris nunc quam venenatis nec</div>
  <div class="btn-outline">Read More</div>
</div>
<div class="service-card abs" style="left:259px">
  <svg class="card-shape" width="168" height="163" viewBox="0 0 168 163"><path d="M0 20Q84 -10 168 20V163H0z" fill="var(--charcoal)"/></svg>
  <div class="service-icon"><svg width="40" height="30" viewBox="0 0 40 30"><path d="M6 22a14 14 0 0128 0z" fill="#222"/><path d="M2 22h36l-2 5H6z" fill="#222"/><path d="M18 9v12M24 10v11" stroke="var(--yellow)" stroke-width="1.4"/></svg></div>
  <div class="service-title">Concreting &amp; Asphalt Work</div>
  <div class="service-copy">Cras a ante vitae enim iaculis aliquam<br>Mauris nunc quam venenatis nec</div>
  <div class="btn-outline">Read More</div>
</div>
<div class="service-card abs" style="left:434px">
  <svg class="card-shape" width="168" height="163" viewBox="0 0 168 163"><path d="M0 20Q84 -10 168 20V163H0z" fill="var(--charcoal)"/></svg>
  <div class="service-icon"><svg width="40" height="30" viewBox="0 0 40 30"><path d="M3 10h26l-5 10H9z" fill="#222"/><path d="M29 10l6-8" stroke="#222" stroke-width="2"/><circle cx="10" cy="24" r="4" fill="none" stroke="#222" stroke-width="2"/><path d="M14 22l10-2" stroke="#222" stroke-width="1.6"/></svg></div>
  <div class="service-title">Additional Services</div>
  <div class="service-copy">Cras a ante vitae enim iaculis aliquam<br>Mauris nunc quam venenatis nec</div>
  <div class="btn-outline">Read More</div>
</div>

<svg class="projects-band abs" width="678" height="210" viewBox="0 0 678 210"><defs><linearGradient id="yel" x1="0" y1="0" x2="1" y2="1"><stop offset="0" stop-color="#fccf0a"/><stop offset="1" stop-color="#ffdf00"/></linearGradient></defs><path d="M0 0H678V177L339 208 0 177z" fill="url(#yel)"/></svg>
<h2 class="projects-heading abs">OUR PROJECTS</h2>
<div class="project-thumb abs" style="left:79px;background:linear-gradient(180deg,#7b7f70,#a9b0b3 50%,#c7cdd0)" role="img" aria-label="Freshly laid wet concrete slab"></div>
<div class="project-thumb abs" style="left:210px;background:linear-gradient(180deg,#8c9298,#7a6a55 45%,#6e5c48)" role="img" aria-label="Crew preparing a gravel base on site"></div>
<div class="project-thumb abs" style="left:341px;background:linear-gradient(180deg,#b8bcb0,#9a6a50 35%,#8c5d45)" role="img" aria-label="Finished red chip driveway"></div>
<div class="project-thumb abs" style="left:472px;background:linear-gradient(180deg,#3f5a35,#5d6d4f 45%,#a4a49c)" role="img" aria-label="Curved concrete path through a garden"></div>
<div class="slider-dots abs"><span class="off"></span><span></span><span></span></div>

<div class="feature-image abs" style="left:80px;background:linear-gradient(180deg,#9bb4cc,#c46a3a 45%,#3f3f45 70%,#2d2d32)" role="img" aria-label="Line of road rollers on new asphalt"></div>
<h3 class="feature-title abs" style="left:212px">Our Services</h3>
<p class="feature-copy abs" style="left:212px;width:130px">Cras a ante vitae enim iaculis aliquam Mauris nunc quam venenatis nec euismod sit amet egestas placerat est lus mus In iaculis facilisis</p>
<div class="read-more abs">READ MORE</div>

<div class="feature-image abs" style="left:350px;width:121px;background:linear-gradient(135deg,#2d2b26,#5a4a20 40%,#c9a318 60%,#3a3a3a)" role="img" aria-label="Paving machine laying asphalt"></div>
<h3 class="feature-title abs" style="left:483px">Contact Us</h3>
<div class="feature-copy abs" style="left:483px;line-height:13.5px">
  Any Questions you would like to ask?<br>Need to talk to us...
  <div class="contact-line"><svg width="6" height="9" viewBox="0 0 6 9"><rect x=".5" y=".5" width="5" height="8" rx="1" fill="none" stroke="#333"/></svg>027 3185904</div>
  <div class="contact-line"><svg width="7" height="7" viewBox="0 0 24 24"><path fill="#333" d="M6.6 10.8a15 15 0 006.6 6.6l2.2-2.2a1 1 0 011-.25 11.4 11.4 0 003.6.6 1 1 0 011 1V20a1 1 0 01-1 1A17 17 0 013 4a1 1 0 011-1h3.5a1 1 0 011 1c0 1.25.2 2.45.6 3.6a1 1 0 01-.25 1z"/></svg>09 41 82 260</div>
</div>

<footer class="site-footer abs"></footer>
<span class="footer-nav abs" style="left:91px">HOME</span>
<span class="footer-nav abs" style="left:135px">ABOUT</span>
<span class="footer-nav abs" style="left:184px">SERVICES</span>
<span class="footer-nav abs" style="left:243px">PROJECTS</span>
<span class="footer-nav abs" style="left:305px">CONTACT</span>
<div class="copyright abs">© 2016 Company Name &nbsp;All right reserved</div>
<span class="social abs" style="left:501px"></span>
<span class="social abs" style="left:525px"></span>
<span class="social abs" style="left:550px"></span>
<span class="social abs" style="left:575px"></span>

</body>
</html>
```